Atelier Marrow Architecture business card

We need to update our business card. We do high end custom residential, hospitality, and wellness architecture. We focus on creating unique spaces and design around the five senses, believing that architecture's true impact is not on our surroundings, but within us. We would like to see designs are instill a sense of calm awe. They should be crisp, fresh, clean, authentic, & contemporary without being sterile, overworked, or harsh. White space is important. Alternative materials are an option if natural. We have created our own logo and would like designs to incorporate it. However, we are willing to see alternatives if the logo becomes a stumbling block and you have an alternate you suggest. Card must have the following information:
Atelier Marrow Architecture, Inc.
728 Holloway Ct. NE Atlanta, GA 30318
Marcus T. Whitcombe, AIA, NCARB, LEED AP BD+C
ateliermarrow.example

Target Market(s)

Higher net worth individuals with an appreciation for design, nature, sustainability,

Industry/Entity Type

Architect

Contact Information for Business Card

See above. The title of Owner or Architect is helpful but not necessary. Minimalism should trump additional information.

Font styles to use
Serif
Sans Serif

Requirements
Must have
• It should look professional. It must use logo
Should not have
• caligraphy, animals, anything that is cute,

```html
<!DOCTYPE html>
<html lang="en">
<head>
<meta charset="utf-8">
<title>Atelier Marrow Architecture — Business Card</title>
<link rel="stylesheet" href="https://fonts.googleapis.com/css2?family=Roboto+Condensed:wght@300;400;700&display=swap">
<style>
  :root {
    --page: #ffffff;
    --paper: #ededed;
    --charcoal: #1f2328;
    --slate: #55585c;
    --orange: #e4862c;
    --white: #ffffff;
    --mist: #c9ccd0;
    --rule: #d9d9d9;
  }
  * { margin: 0; padding: 0; box-sizing: border-box; }
  html, body {
    width: 900px; height: 1200px; overflow: hidden;
    background: var(--page);
    font-family: "Roboto Condensed", Arial, sans-serif;
  }
  .sheet { position: relative; width: 900px; height: 1200px; }

  .card { position: absolute; left: 202.5px; width: 444px; overflow: hidden; background: var(--paper); }
  .card--front { top: 277.5px; height: 285px; }
  .card--back  { top: 637.5px; height: 283.5px; }
  .card svg.shapes { position: absolute; inset: 0; }

  .wordmark {
    position: absolute; text-align: center; color: var(--slate);
    font-weight: 300; text-transform: uppercase; line-height: 1;
  }
  .wordmark__name { display: block; }
  .wordmark__practice { display: block; }

  .card--front .wordmark { left: 0; width: 444px; top: 108px; }
  .card--front .wordmark__name { font-size: 21px; letter-spacing: 5px; }
  .card--front .wordmark__practice { font-size: 8px; letter-spacing: 7.5px; margin-top: 7px; }

  .card--back .wordmark { left: 259.5px; width: 184.5px; top: 52px; }
  .card--back .wordmark__name { font-size: 12.5px; letter-spacing: 2.6px; }
  .card--back .wordmark__practice { font-size: 5px; letter-spacing: 4.4px; margin-top: 4px; }

  .holder {
    position: absolute; right: 211px; top: 34px; text-align: right;
    color: var(--white); line-height: 1;
  }
  .holder__name { font-size: 24px; font-weight: 400; letter-spacing: 0.2px; white-space: nowrap; }
  .holder__credentials {
    margin-top: 6px; font-size: 7px; font-weight: 400; letter-spacing: 0.8px;
    color: var(--mist); white-space: nowrap;
  }

  .contact {
    position: absolute; right: 207px; text-align: right;
    color: var(--white); font-size: 6.5px; font-weight: 700; line-height: 1;
    white-space: nowrap; letter-spacing: 0.2px;
  }
  .contact--address { top: 109px; }
  .contact--phone   { top: 141px; }
  .contact--email   { top: 177px; }
  .contact--web     { top: 216px; }
</style>
</head>
<body>
<main class="sheet">

  <section class="card card--front" aria-label="Card front">
    <svg class="shapes" width="444" height="285" viewBox="0 0 444 285" aria-hidden="true">
      <rect class="top-band" x="0" y="0" width="444" height="7.5" fill="var(--charcoal)"/>
      <rect class="base-band" x="0" y="235.5" width="444" height="49.5" fill="var(--charcoal)"/>
      <polygon class="corner-block" points="330,213 444,213 444,235.5 318,235.5" fill="var(--charcoal)"/>
      <polygon class="corner-fold" points="318,228 330,213 339,213 327,228" fill="var(--slate)"/>
      <polygon class="accent-band" points="139.5,228 444,228 444,262.5 123,262.5" fill="var(--orange)"/>
    </svg>
    <div class="wordmark">
      <span class="wordmark__name">Atelier Marrow</span>
      <span class="wordmark__practice">Architecture</span>
    </div>
  </section>

  <section class="card card--back" aria-label="Card back">
    <svg class="shapes" width="444" height="283.5" viewBox="0 0 444 283.5" aria-hidden="true">
      <rect class="info-panel" x="0" y="0" width="241.5" height="283.5" fill="var(--charcoal)"/>
      <rect class="icon-rail" x="241.5" y="0" width="18" height="283.5" fill="var(--rule)"/>
      <rect class="rail-cap" x="241.5" y="0" width="18" height="60" fill="var(--orange)"/>
      <rect class="rail-foot" x="241.5" y="244.5" width="18" height="39" fill="var(--orange)"/>

      <g class="contact-lines" stroke="var(--white)" stroke-width="0.8">
        <line x1="124.5" y1="150" x2="237" y2="150"/>
        <line x1="124.5" y1="186" x2="237" y2="186"/>
        <line x1="124.5" y1="225" x2="237" y2="225"/>
      </g>

      <g class="icon icon--address" transform="translate(241.5 103.5)">
        <rect width="18" height="18" fill="var(--orange)"/>
        <path d="M9 3.5 L15 9 H13.2 V14.5 H10.5 V11 H7.5 V14.5 H4.8 V9 H3 Z" fill="var(--white)"/>
      </g>
      <g class="icon icon--phone" transform="translate(241.5 139.5)">
        <rect width="18" height="18" fill="var(--white)"/>
        <path d="M6 4.5 L7.8 4.5 L8.6 7.2 L7.4 8.2 Q8.4 10.4 10.3 11.4 L11.3 10.2 L14 11 L14 12.8 Q13.3 14 11.5 13.6 Q6.5 12.2 4.6 6.5 Q4.5 5 6 4.5 Z" fill="var(--charcoal)"/>
      </g>
      <g class="icon icon--send" transform="translate(241.5 175.5)">
        <rect width="18" height="18" fill="var(--orange)"/>
        <path d="M4 4 L14.5 9 L4 14 L6 9 Z" fill="var(--white)"/>
      </g>
      <g class="icon icon--web" transform="translate(241.5 214.5)">
        <rect width="18" height="18" fill="var(--white)"/>
        <circle cx="9" cy="9" r="5.5" fill="var(--charcoal)"/>
        <g stroke="var(--white)" stroke-width="0.6" fill="none">
          <line x1="3.5" y1="9" x2="14.5" y2="9"/>
          <ellipse cx="9" cy="9" rx="2.3" ry="5.5"/>
        </g>
      </g>
    </svg>

    <div class="holder">
      <h1 class="holder__name">Marcus T. Whitcombe</h1>
      <p class="holder__credentials">AIA, NCARB, LEED AP BD+C</p>
    </div>

    <p class="contact contact--address">728 Holloway Ct. NE Atlanta, GA 30318</p>
    <p class="contact contact--phone">404.555.0172</p>
    <p class="contact contact--email">marcus@ateliermarrow.example</p>
    <p class="contact contact--web">ateliermarrow.example</p>

    <div class="wordmark">
      <span class="wordmark__name">Atelier Marrow</span>
      <span class="wordmark__practice">Architecture</span>
    </div>
  </section>

</main>
</body>
</html>
```